E-mail Ad Design Project

I would like a lower banner ad designed for placement within an e-mail. The size has to be 450px x 230px (6in x 3.07in) and must be either a GIF or JPEG, not to exceed 30K.

We are a medical billing company that provides services to physical therapy practices in Florida, and this ad is intended for owners and office managers of physical therapy businesses. We provide therapy offices with practice management software, submit medical claims on behalf of their patients, follow-up with insurance companies on outstanding claims, and also perform necessary back-end collections with patient balances. We also are able to interface with popular therapy documentation products to streamline data entry.

The design colors should incorporate our logo and red/blue colors (see www.harborlinebilling.net).

Target Market(s)

Physical therapists and administrators of physical therapy offices

Industry/Entity Type

Physical Therapy

Requirements
Must have
• Grabbing/heading text:

Tired of Denials and Confusing Rejection Codes?
We Take the Pain Out of Medical Billing.

Offer:

Get Started Today with 2 Free Months of Billing
Nice to have
• We provide services mainly to Florida therapists, so it would be nice to have an image or text that highlights this fact. Also, the e-mail campaign this is a part of will be sent to Florida recipients.

```html
<!DOCTYPE html>
<html lang="en">
<head>
<meta charset="utf-8">
<title>Medical Billing Email Banners</title>
<link href="https://fonts.googleapis.com/css2?family=Alfa+Slab+One&family=Lato:wght@400;700&display=swap" rel="stylesheet">
<style>
  :root {
    --stage: #2b2b2b;
    --blue-deep: #0a3f95;
    --blue-mid: #1466c4;
    --blue-light: #2a9be0;
    --white: #ffffff;
    --photo-light: #eef2f5;
    --photo-mid: #c9d3dc;
    --photo-edge: #0d4fa8;
    --ribbon-red: #e0151b;
    --ribbon-red-dark: #b20d12;
    --ribbon-green: #7bb324;
    --ribbon-green-dark: #5a8c14;
    --ink-shadow: #1a1a1a;
  }
  * { margin: 0; padding: 0; box-sizing: border-box; }
  html, body { width: 988px; height: 1200px; overflow: hidden; }
  body { background: var(--stage); position: relative; }

  .banner {
    position: absolute;
    left: 185px;
    width: 620px;
    height: 317px;
    overflow: hidden;
    background: linear-gradient(120deg, var(--blue-deep) 0%, var(--blue-mid) 45%, var(--blue-light) 100%);
  }
  .banner--one { top: 101px; }
  .banner--two { top: 453px; }
  .banner--three { top: 805px; }

  .banner__photo {
    position: absolute;
    right: 0; top: 0;
    width: 250px; height: 317px;
    border-top-left-radius: 300px 317px;
    border-bottom-left-radius: 160px 200px;
    border-left: 6px solid var(--photo-edge);
    background: linear-gradient(160deg, var(--photo-light) 0%, var(--photo-mid) 100%);
  }

  .banner__headline {
    position: absolute;
    left: 14px; top: 14px;
    font-family: "Alfa Slab One", serif;
    color: var(--white);
    text-transform: uppercase;
    font-size: 31px;
    line-height: 48px;
    letter-spacing: 0.5px;
  }
  .banner__headline span { display: block; }
  .banner--one .banner__headline span:nth-child(2) { font-size: 36px; }
  .banner--two .banner__headline,
  .banner--three .banner__headline {
    letter-spacing: 1.5px;
    text-shadow: 1px 1px 0 var(--ink-shadow), 2px 2px 0 var(--ink-shadow), 3px 3px 2px rgba(0,0,0,.5);
  }

  .banner__tagline {
    position: absolute;
    left: 14px; top: 176px;
    font-family: "Lato", sans-serif;
    font-size: 26px;
    line-height: 35px;
    color: var(--white);
  }

  .banner__offer {
    position: absolute;
    left: 301px; top: 246px;
    width: 319px; height: 62px;
    clip-path: polygon(0 0, 100% 0, 100% 100%, 0 100%, 6% 50%);
    font-family: "Lato", sans-serif;
    color: var(--white);
    text-align: center;
    padding-left: 20px;
  }
  .banner__offer--red { background: linear-gradient(180deg, var(--ribbon-red) 0%, var(--ribbon-red-dark) 100%); }
  .banner__offer--green { background: linear-gradient(180deg, var(--ribbon-green) 0%, var(--ribbon-green-dark) 100%); }
  .banner__offer-lead { display: block; font-size: 16px; font-weight: 700; padding-top: 6px; }
  .banner__offer-main { display: block; font-size: 22px; font-weight: 700; line-height: 26px; }
</style>
</head>
<body>

<section class="banner banner--one">
  <div class="banner__photo" role="img" aria-label="Photo of a doctor in a white coat reviewing a chart at a laptop"></div>
  <h2 class="banner__headline"><span>Tired of Denials</span><span>and Confusing</span><span>Rejection Codes?</span></h2>
  <p class="banner__tagline">We Take the Pain Out<br>of Medical Billing.</p>
  <div class="banner__offer banner__offer--red">
    <span class="banner__offer-lead">Get Started Today with</span>
    <span class="banner__offer-main">2 Free Months of Billing</span>
  </div>
</section>

<section class="banner banner--two">
  <div class="banner__photo" role="img" aria-label="Photo of a doctor in a white coat reviewing a chart at a laptop"></div>
  <h2 class="banner__headline"><span>Tired of Denials</span><span>and Confusing</span><span>Rejection Codes?</span></h2>
  <p class="banner__tagline">We Take the Pain Out<br>of Medical Billing.</p>
  <div class="banner__offer banner__offer--green">
    <span class="banner__offer-lead">Get Started Today with</span>
    <span class="banner__offer-main">2 Free Months of Billing</span>
  </div>
</section>

<section class="banner banner--three">
  <div class="banner__photo" role="img" aria-label="Photo of a doctor in a white coat reviewing a chart at a laptop"></div>
  <h2 class="banner__headline"><span>Tired of Denials</span><span>and Confusing</span><span>Rejection Codes?</span></h2>
  <p class="banner__tagline">We Take the Pain Out<br>of Medical Billing.</p>
  <div class="banner__offer banner__offer--red">
    <span class="banner__offer-lead">Get Started Today with</span>
    <span class="banner__offer-main">2 Free Months of Billing</span>
  </div>
</section>

</body>
</html>
```